Business Card - Rebranding for Consulting Firm

We are renaming and rebranding our consulting firm and need to raise the level of quality of our cards as part of that effort. We consult to leading high tech, life science and other innovation sector companies.

Need a two-sided business card design.

Side 1: (a) Company logo (b) tag line: Optimize Your Investment in Talent (c) Name (d) Title (e) Phone 1: Office (f) Phone 2: Mobile (g) email: person@HollowmereAdvisory.com

Side 2: Two lines of text: (a) Growth is Imperative. Change is Constant. Talent Executes Strategy. (b) We help you excel at all three.

Target Market(s)

Business and human resources executives and senior managers

Industry/Entity Type

Management Consulting

Contact Information for Business Card

Font styles to use
Sans Serif

Requirements
Must have
• clean, not too busy, but with a bit of creativity. Stick to the colors used in the attached logo
• appeal to high tech, life science companies
Nice to have
• prefer white background

```html
<!DOCTYPE html>
<html lang="en">
<head>
<meta charset="utf-8">
<title>Hollowmere Advisory – Business Card</title>
<link rel="stylesheet" href="https://fonts.googleapis.com/css2?family=Lato:wght@400;700&display=swap">
<style>
  :root {
    --page-bg: #e8e9eb;
    --brand-blue: #0b6aa2;
    --brand-sky: #00a3e0;
    --brand-teal: #0a86b8;
    --ink-gray: #555b61;
    --soft-gray: #7a7f84;
    --back-gray: #808182;
    --white: #ffffff;
  }
  * { margin: 0; padding: 0; box-sizing: border-box; }
  html, body {
    width: 1200px; height: 987px; overflow: hidden;
    background: var(--page-bg);
    font-family: "Lato", sans-serif;
  }
  .canvas { position: relative; width: 1200px; height: 987px; }
  .card {
    position: absolute; left: 293px; width: 615px; height: 350px;
    overflow: hidden;
    box-shadow: 0 6px 18px rgba(0,0,0,0.18);
  }
  .card--front { top: 130px; background: var(--white); }
  .card--back { top: 505px; background: var(--back-gray); }

  .brand-name {
    position: absolute; left: 29px; top: 46px;
    font-size: 34px; font-weight: 700; letter-spacing: -0.3px;
    color: var(--brand-blue);
    display: flex; align-items: center; gap: 10px;
  }
  .brand-name .mark-square {
    width: 22px; height: 22px; background: var(--brand-sky);
  }

  .person { position: absolute; left: 26px; top: 116px; }
  .person__name { font-size: 22px; font-weight: 700; color: var(--brand-blue); line-height: 1.2; }
  .person__title { font-size: 16px; color: var(--soft-gray); margin-top: 2px; }

  .contact-list { position: absolute; left: 26px; top: 183px; list-style: none; }
  .contact-list li {
    display: flex; align-items: center; gap: 6px;
    height: 23.5px; font-size: 15.5px; color: var(--ink-gray);
  }
  .contact-list svg { width: 16px; height: 16px; fill: var(--brand-blue); flex: none; }

  .tagline {
    position: absolute; left: 26px; top: 284px;
    font-size: 15.5px; font-weight: 700; color: var(--brand-blue);
  }

  .growth-visual {
    position: absolute; left: 330px; top: 80px; width: 285px; height: 245px;
    background: linear-gradient(135deg, rgba(0,163,224,0.10) 0%, rgba(10,134,184,0.35) 55%, rgba(11,106,162,0.55) 100%);
  }

  .front-band {
    position: absolute; left: 0; bottom: 0; width: 100%; height: 25px;
    background: var(--brand-blue);
  }

  .back-brand {
    position: absolute; left: 0; top: 154px; width: 100%;
    display: flex; justify-content: center; align-items: center; gap: 12px;
    font-size: 44px; font-weight: 700; color: var(--white); letter-spacing: -0.4px;
  }
  .back-brand .mark-square { width: 28px; height: 28px; background: var(--white); }

  .back-message {
    position: absolute; left: 0; top: 278px; width: 100%;
    text-align: center; color: var(--white);
    font-size: 15px; line-height: 21px;
  }
</style>
</head>
<body>
<main class="canvas">

  <section class="card card--front" aria-label="Business card front">
    <div class="brand-name"><span class="mark-square"></span>Hollowmere Advisory</div>

    <div class="person">
      <p class="person__name">Aaron Vale</p>
      <p class="person__title">President</p>
    </div>

    <ul class="contact-list">
      <li>
        <svg viewBox="0 0 16 16" aria-hidden="true"><path d="M2 5c0-2 2-3 6-3s6 1 6 3v1h-3V5H5v1H2zM4 7h8l2 6H2zm4 1.5a2 2 0 1 0 0 4 2 2 0 0 0 0-4z"/></svg>
        555 0142 7781
      </li>
      <li>
        <svg viewBox="0 0 16 16" aria-hidden="true"><path d="M5 1h6a1 1 0 0 1 1 1v12a1 1 0 0 1-1 1H5a1 1 0 0 1-1-1V2a1 1 0 0 1 1-1zm1 2v9h4V3zm2 10a.8.8 0 1 0 0 1.6.8.8 0 0 0 0-1.6z"/></svg>
        555 0199 3264
      </li>
      <li>
        <svg viewBox="0 0 16 16" aria-hidden="true"><path d="M1 4h14v1L8 9 1 5zm0 2.3 7 4 7-4V12H1z"/></svg>
        person@HollowmereAdvisory.com
      </li>
      <li>
        <svg viewBox="0 0 16 16" aria-hidden="true"><path d="M8 1a7 7 0 1 0 0 14A7 7 0 0 0 8 1zm-1 2.2c-.6 1-.3 2 .5 2.3.9.3.4 1.4-.4 1.7-.9.3-1.6 1-1.3 2 .3.8.2 2-.5 2.6A5.3 5.3 0 0 1 7 3.2zm3 1c1 .2 2.4 1.5 2.9 3-.8-.3-1.7 0-2.1.7-.5.8-1.5.4-1.6-.5-.1-1 .6-1.5.8-2.2z"/></svg>
        www.HollowmereAdvisory.com
      </li>
    </ul>

    <p class="tagline">Optimize Your Investment in Talent</p>

    <div class="growth-visual" role="img" aria-label="Decorative rising growth graphic in brand blues"></div>
    <div class="front-band"></div>
  </section>

  <section class="card card--back" aria-label="Business card back">
    <div class="back-brand"><span class="mark-square"></span>Hollowmere Advisory</div>
    <p class="back-message">
      Growth is Imperative. Change is Constant. Talent Executes Strategy.<br>
      We help you excel at all three.
    </p>
  </section>

</main>
</body>
</html>
```